I need a book cover designed for my e-book The Corner Shop Falcon.

The Corner Shop Falcon is a book about how to turn any small business into a success and is based on my experience building a cocktail bar. I am led in my journey by a stylish Japanese business expert in a sharp suit and a top knot.

The final design should stand out and grab people's attention while conveying the simplicity of the samurai.

I have attached a cover that I wish I could use (but obviously can't because of copyright).

I will need a JPEG file and at least 2500 pixels on the longest side with a height/weight ratio of 1.6

```html
<!DOCTYPE html>
<html lang="en">
<head>
<meta charset="UTF-8">
<title>The Corner Shop Falcon — Book Cover</title>
<link rel="stylesheet" href="https://fonts.googleapis.com/css2?family=Allura&family=Cinzel:wght@500;700&family=Shojumaru&family=Montserrat:wght@700&display=swap">
<style>
  :root {
    --stage: #e7e2da;
    --burst-core: #fffbe0;
    --burst-mid: #ffe56a;
    --burst-warm: #f9b935;
    --burst-edge: #f08a24;
    --ink: #111111;
    --paper: #ffffff;
    --figure-dark: #1f2c38;
    --figure-accent: #b3191c;
  }
  * { margin: 0; padding: 0; box-sizing: border-box; }
  html, body {
    width: 1200px;
    height: 800px;
    overflow: hidden;
    background: var(--stage);
  }
  .canvas {
    width: 1200px;
    height: 800px;
    display: flex;
    justify-content: center;
    align-items: center;
  }
  .cover {
    position: relative;
    width: 566px;
    height: 800px;
    overflow: hidden;
    background:
      repeating-conic-gradient(from 0deg at 50% 62%,
        rgba(255,255,255,0.22) 0deg 3deg,
        rgba(255,255,255,0) 3deg 11deg),
      radial-gradient(circle at 50% 62%,
        var(--burst-core) 0%,
        var(--burst-mid) 28%,
        var(--burst-warm) 60%,
        var(--burst-edge) 100%);
  }
  .title {
    position: absolute;
    left: 0;
    top: 22px;
    width: 100%;
    height: 250px;
  }
  .title-script {
    position: absolute;
    left: 82px;
    top: 0;
    font-family: "Allura", cursive;
    font-size: 118px;
    line-height: 1;
    color: var(--ink);
    transform: rotate(-4deg);
    white-space: nowrap;
  }
  .title-brush {
    position: absolute;
    left: 0;
    width: 100%;
    top: 150px;
    text-align: center;
    font-family: "Shojumaru", cursive;
    font-size: 84px;
    line-height: 1;
    color: var(--ink);
    letter-spacing: 2px;
  }
  .title-serif {
    position: absolute;
    left: 0;
    width: 100%;
    top: 120px;
    text-align: center;
    font-family: "Cinzel", serif;
    font-weight: 500;
    font-size: 76px;
    line-height: 1;
    color: var(--paper);
    text-shadow: 2px 3px 4px rgba(0,0,0,0.55);
    letter-spacing: 1px;
  }
  .subtitle {
    position: absolute;
    left: 0;
    top: 282px;
    width: 100%;
    text-align: center;
    font-family: "Montserrat", sans-serif;
    font-weight: 700;
    font-size: 13px;
    line-height: 18px;
    letter-spacing: 0.32em;
    color: var(--ink);
    text-transform: uppercase;
  }
  .figure {
    position: absolute;
    left: 168px;
    top: 362px;
    width: 244px;
    height: 346px;
  }
  .author {
    position: absolute;
    left: 0;
    bottom: 30px;
    width: 100%;
    text-align: center;
    font-family: "Cinzel", serif;
    font-weight: 700;
    font-size: 42px;
    letter-spacing: 1px;
    color: var(--ink);
  }
</style>
</head>
<body>
  <main class="canvas">
    <section class="cover">
      <h1 class="title">
        <span class="title-script">The Corner</span>
        <span class="title-brush">Falcon</span>
        <span class="title-serif">SHOP</span>
      </h1>
      <p class="subtitle">Cutting through the crap to help<br>you and your business to be<br>the success you deserve</p>
      <svg class="figure" viewBox="0 0 244 346" role="img" aria-label="Cartoon business warrior in a dark suit with a red tie and scarf, crouching and drawing a sword">
        <defs>
          <linearGradient id="figure-tone" x1="0" y1="0" x2="0" y2="1">
            <stop offset="0" stop-color="var(--figure-dark)" stop-opacity="0.85"/>
            <stop offset="0.7" stop-color="var(--figure-dark)" stop-opacity="0.7"/>
            <stop offset="1" stop-color="var(--figure-accent)" stop-opacity="0.35"/>
          </linearGradient>
        </defs>
        <rect x="0" y="0" width="244" height="346" rx="28" fill="url(#figure-tone)"/>
      </svg>
      <p class="author">MARTIN HALE</p>
    </section>
  </main>
</body>
</html>
```